Solar Advertising Flier to generate Biz

I need a advertisement that generates business to be used in a mailer for marketing purposes.

Im attaching a file that is a an idea of advertisement.
I do not want the "ZVN" specific information on it.
I want the background solar panels.
Same information as the ad.
And I've attached my Logo - I want the color scheme to match this.

Thank you

Target Market(s)

Middle to Upper Class Home Owners

Industry/Entity Type

Solar Energy

Requirements
Must have
• A call to action
• A professional look
Nice to have
• A family
• Great looking solar panels
Should not have
• Cartoons

```html
<!DOCTYPE html>
<html lang="en">
<head>
<meta charset="utf-8">
<title>Go Solar – Bright Horizon Energy Flier</title>
<link rel="stylesheet" href="https://fonts.googleapis.com/css2?family=Oswald:wght@500;600;700&family=Roboto+Condensed:wght@400;700&display=swap">
<style>
  :root {
    --page-bg: #eeeae4;
    --photo-top: #1d78d2;
    --photo-bottom: #2a5ea8;
    --backdrop-a: #a4d2f1;
    --backdrop-b: #d6ecf9;
    --brand-blue: #1a7fd6;
    --brand-green: #8dc63f;
    --badge-green: #6fae24;
    --ink: #1d2a33;
    --white: #ffffff;
    --ring-grey: #d9dcdf;
  }
  * { box-sizing: border-box; margin: 0; padding: 0; }
  html, body { width: 1200px; height: 1200px; overflow: hidden; }
  body { background: var(--page-bg); position: relative; font-family: "Roboto Condensed", Arial, sans-serif; }

  .flier { position: absolute; left: 190px; top: 0; width: 820px; height: 1200px; overflow: hidden; background: var(--backdrop-b); }
  .flier-art { position: absolute; inset: 0; width: 820px; height: 1200px; }

  .headline {
    position: absolute; left: 52px; top: 40px;
    font-family: "Oswald", "Arial Narrow", sans-serif; font-weight: 600;
    font-size: 168px; line-height: 0.92; color: var(--white);
    letter-spacing: -2px; text-transform: uppercase;
    text-shadow: 0 3px 6px rgba(0,0,0,0.18);
  }

  .brand { position: absolute; left: 560px; top: 66px; width: 210px; text-align: center; color: var(--white); }
  .brand-mark { width: 92px; height: 92px; margin: 0 auto 12px; border: 6px solid var(--white); border-radius: 50%; }
  .brand-name { font-family: "Roboto Condensed", Arial, sans-serif; font-weight: 400; font-size: 27px; line-height: 1.05; letter-spacing: 1px; text-transform: uppercase; }

  .rebate {
    position: absolute; left: 58px; top: 487px; width: 206px; height: 206px;
    border-radius: 50%; background: var(--ring-grey); padding: 10px;
    box-shadow: 0 4px 10px rgba(0,0,0,0.25);
  }
  .rebate-inner {
    width: 100%; height: 100%; border-radius: 50%;
    background: radial-gradient(circle at 45% 40%, #8fd13a, var(--badge-green));
    display: flex; flex-direction: column; align-items: center; justify-content: center; padding-top: 18px;
  }
  .rebate-amount { font-family: "Oswald", sans-serif; font-weight: 700; font-size: 60px; line-height: 1; color: var(--white); text-shadow: 0 2px 2px rgba(0,0,0,0.25); }
  .rebate-label { font-family: "Oswald", sans-serif; font-weight: 600; font-size: 21px; color: #1f2f12; letter-spacing: 0.5px; }

  .benefits { position: absolute; left: 49px; top: 748px; width: 306px; list-style: none; }
  .benefit {
    height: 54px; margin-bottom: 32px; background: var(--brand-blue); border-radius: 8px;
    display: flex; align-items: center; padding: 0 12px 0 16px; gap: 12px;
    color: var(--white); font-weight: 700; font-size: 14.5px; line-height: 1.1;
    box-shadow: 0 2px 4px rgba(0,0,0,0.15);
  }
  .benefit::before { content: ""; flex: 0 0 12px; height: 12px; border-radius: 50%; background: var(--white); border: 2px solid #cde3f6; }

  .how-it-works {
    position: absolute; left: 465px; top: 807px; width: 238px; height: 238px; border-radius: 50%;
    background: var(--white);
    border: 9px solid var(--brand-blue); border-bottom-color: var(--brand-green); border-left-color: var(--brand-green);
    transform: rotate(-45deg);
  }
  .how-it-works-body {
    position: absolute; inset: 0; transform: rotate(45deg);
    display: flex; flex-direction: column; align-items: center; justify-content: center;
    padding: 0 26px; text-align: center;
  }
  .how-title { color: var(--brand-blue); font-size: 16px; font-weight: 400; text-transform: uppercase; margin-bottom: 2px; }
  .how-text { color: #333; font-size: 12.6px; line-height: 1.3; }

  .contact-bar {
    position: absolute; left: 0; bottom: 0; width: 820px; height: 109px; background: var(--brand-green);
    display: flex; align-items: center; padding: 0 24px 0 30px;
  }
  .cta { width: 312px; }
  .cta-line { font-size: 12.5px; font-weight: 400; color: var(--ink); text-transform: uppercase; }
  .cta-phone { font-family: "Oswald", sans-serif; font-weight: 500; font-size: 46px; line-height: 1.1; color: var(--white); letter-spacing: 1px; }
  .divider { width: 1px; height: 60px; background: rgba(29,42,51,0.45); margin: 0 18px; }
  .address { width: 180px; text-align: center; font-size: 14px; line-height: 1.7; color: var(--ink); font-weight: 700; white-space: nowrap; }
  .website { flex: 1; text-align: center; font-size: 14px; color: var(--ink); font-weight: 700; }
</style>
</head>
<body>
  <main class="flier">
    <svg class="flier-art" viewBox="0 0 820 1200">
      <defs>
        <linearGradient id="photoFill" x1="0" y1="0" x2="0" y2="1">
          <stop offset="0" stop-color="var(--photo-top)"/>
          <stop offset="1" stop-color="var(--photo-bottom)"/>
        </linearGradient>
        <linearGradient id="backdropFill" x1="0" y1="0" x2="1" y2="1">
          <stop offset="0" stop-color="var(--backdrop-a)"/>
          <stop offset="1" stop-color="var(--backdrop-b)"/>
        </linearGradient>
      </defs>
      <rect x="0" y="0" width="820" height="1200" fill="url(#backdropFill)" role="img" aria-label="Photo: close-up of solar panels reflecting a bright sky"/>
      <path d="M0 482 C120 612 330 764 530 764 C660 764 765 690 820 560 V0 H0 Z" fill="var(--brand-blue)"/>
      <path d="M0 460 C120 590 330 742 530 742 C655 742 762 670 820 540 V0 H0 Z" fill="var(--brand-green)"/>
      <path d="M0 430 C120 560 330 710 530 710 C650 710 760 640 820 510 V0 H0 Z" fill="url(#photoFill)" role="img" aria-label="Photo: solar farm under a blue sky beside the sea"/>
    </svg>

    <h1 class="headline">Go<br>Solar</h1>

    <div class="brand">
      <div class="brand-mark"></div>
      <div class="brand-name">Bright Horizon<br>Energy</div>
    </div>

    <div class="rebate">
      <div class="rebate-inner">
        <span class="rebate-amount">$500</span>
        <span class="rebate-label">CASH REBATE</span>
      </div>
    </div>

    <ul class="benefits">
      <li class="benefit">$0 Down, no upfront cost.</li>
      <li class="benefit">Save up to 90% off your utility bill.</li>
      <li class="benefit">Protect against inflation &amp; energy costs increases from your Utility Company.</li>
      <li class="benefit">Provide clean, reliable energy for your family powered by the sun.</li>
    </ul>

    <section class="how-it-works">
      <div class="how-it-works-body">
        <h2 class="how-title">How it works...</h2>
        <p class="how-text">Your solar system allows you to generate your own clean power and COSTS LESS than your current utility company. Simply pay by the month, like you do now...but at a LOWER rate and START SAVING IMMEDIATELY.</p>
      </div>
    </section>

    <footer class="contact-bar">
      <div class="cta">
        <div class="cta-line">Call today for a no obligation consultation</div>
        <div class="cta-phone">555-014-2287</div>
      </div>
      <div class="divider"></div>
      <div class="address">4410 W Canyon Rd B-210<br>Sunvale AZ 85001</div>
      <div class="divider"></div>
      <div class="website">www.BrightHorizonEnergy.com</div>
    </footer>
  </main>
</body>
</html>
```